Global Nano Technology Surface Protection company needs a new logo and cards

We are a Global company that will apply nanotechnology coatings on surfaces to prevent growth and spread of bacteria, viruses, mold etc. We deal with large corporates, airlines, hospitals and schools so we are after a new modern, simple and clean look that will have great visual impact.
We a company that is focused on prevention and protection.

Company name, Quorvane Systems Worldwide

Subtext, Antimicrobial Surface Protection

Logo, QVSW or QSW

Target Market(s)

Hospitals, Transport agencies, Airlines, Corporate entities

Industry/Entity Type

Protection

Contact Information for Business Card

Logo, QVSW or QSW
www.qvsw-example.us
Derek Holloway
+64290536218
tidyshieldnz@mailbox-example.com

Logo Text

QVSW

Requirements
Must have
• Simple clean look
Should not have
• Nothing too messy

```html
<!DOCTYPE html>
<html lang="en">
<head>
<meta charset="utf-8">
<title>Quorvane Systems Worldwide — Business Cards</title>
<link rel="stylesheet" href="https://fonts.googleapis.com/css2?family=Montserrat:wght@400;500;700;800&display=swap">
<style>
  :root {
    --page-bg: #e4e4e4;
    --card-bg: #1c1c1c;
    --brand-blue: #1fa3e3;
    --text-white: #ffffff;
    --text-soft: #cfcfcf;
  }
  html, body {
    margin: 0;
    padding: 0;
    width: 1200px;
    height: 900px;
    overflow: hidden;
    background: var(--page-bg);
    font-family: "Montserrat", sans-serif;
  }
  .stage {
    width: 1200px;
    height: 900px;
    display: flex;
    align-items: center;
    justify-content: center;
    gap: 90px;
  }
  .card {
    position: relative;
    width: 330px;
    height: 576px;
    background: var(--card-bg);
    border-radius: 4px;
    box-shadow: 0 18px 40px rgba(0,0,0,0.25);
    box-sizing: border-box;
    color: var(--text-white);
  }
  .brand {
    position: absolute;
    left: 0;
    right: 0;
    display: flex;
    flex-direction: column;
    align-items: center;
    text-align: center;
  }
  .card--front .brand { top: 200px; }
  .card--back .brand { top: 70px; }
  .brand__mark {
    display: flex;
    align-items: center;
    gap: 10px;
  }
  .brand__square {
    width: 14px;
    height: 14px;
    background: var(--brand-blue);
  }
  .brand__name {
    font-weight: 800;
    font-size: 58px;
    letter-spacing: 1px;
    line-height: 1;
    color: var(--text-white);
  }
  .brand__company {
    margin-top: 12px;
    font-weight: 700;
    font-size: 15px;
    line-height: 1.3;
  }
  .brand__company span {
    display: block;
    font-weight: 400;
    font-size: 15px;
  }
  .brand__tagline {
    margin-top: 6px;
    font-size: 8.5px;
    letter-spacing: 0.6px;
    color: var(--text-soft);
    text-transform: uppercase;
  }
  .contact {
    position: absolute;
    left: 44px;
    right: 24px;
    top: 330px;
  }
  .contact__name {
    font-size: 28px;
    font-weight: 500;
    color: var(--brand-blue);
    margin: 0 0 18px;
  }
  .contact__list {
    list-style: none;
    margin: 0;
    padding: 0 0 0 6px;
  }
  .contact__item {
    display: flex;
    align-items: center;
    gap: 10px;
    font-size: 12.5px;
    color: var(--text-white);
    margin-bottom: 8px;
  }
  .contact__icon {
    width: 12px;
    height: 12px;
    flex: none;
  }
</style>
</head>
<body>
<main class="stage">
  <section class="card card--front" aria-label="Card front">
    <div class="brand">
      <div class="brand__mark">
        <div class="brand__square"></div>
        <div class="brand__name">QVSW</div>
      </div>
      <div class="brand__company">Quorvane Systems<span>Worldwide</span></div>
      <div class="brand__tagline">Antimicrobial Surface Protection</div>
    </div>
  </section>

  <section class="card card--back" aria-label="Card back">
    <div class="brand">
      <div class="brand__mark">
        <div class="brand__square"></div>
        <div class="brand__name">QVSW</div>
      </div>
      <div class="brand__company">Quorvane Systems<span>Worldwide</span></div>
      <div class="brand__tagline">Antimicrobial Surface Protection</div>
    </div>

    <div class="contact">
      <h2 class="contact__name">Derek Holloway</h2>
      <ul class="contact__list">
        <li class="contact__item">
          <svg class="contact__icon" viewBox="0 0 24 24" aria-hidden="true"><path fill="#1fa3e3" d="M6.6 10.8a15.1 15.1 0 0 0 6.6 6.6l2.2-2.2a1 1 0 0 1 1-.25 11.4 11.4 0 0 0 3.6.57 1 1 0 0 1 1 1V20a1 1 0 0 1-1 1A17 17 0 0 1 3 4a1 1 0 0 1 1-1h3.5a1 1 0 0 1 1 1c0 1.25.2 2.45.57 3.57a1 1 0 0 1-.25 1z"/></svg>
          +64290536218
        </li>
        <li class="contact__item">
          <svg class="contact__icon" viewBox="0 0 24 24" aria-hidden="true"><rect x="2.5" y="5" width="19" height="14" rx="1.5" fill="none" stroke="#1fa3e3" stroke-width="2"/><path d="M3 6l9 7 9-7" fill="none" stroke="#1fa3e3" stroke-width="2"/></svg>
          tidyshieldnz@mailbox-example.com
        </li>
        <li class="contact__item">
          <svg class="contact__icon" viewBox="0 0 24 24" aria-hidden="true"><circle cx="12" cy="12" r="9.5" fill="none" stroke="#1fa3e3" stroke-width="2"/><ellipse cx="12" cy="12" rx="4" ry="9.5" fill="none" stroke="#1fa3e3" stroke-width="1.8"/><path d="M2.5 12h19" stroke="#1fa3e3" stroke-width="1.8"/></svg>
          www.qvsw-example.us
        </li>
      </ul>
    </div>
  </section>
</main>
</body>
</html>
```